CedarBight.Lawyer, a new website for Morris.

Looking for a professional web site for my small country law firm.
I have a logo, chart, map, my photo, office photo, google analytics code, my drone video on YouTube, "Brantwell Beacon Skyrun, also on www.loftcove.guide", and text content. I am figuring out how to get those into digital forms.
First page needs a professional look. Here's where I am really hoping for your skill set.
Banner should be well designed so as to "ease" the viewer into confidence in my firm
Prefer the "white backround", less cluttered style of design.
My office has been in Key Center, main and only town of Key Peninsula, for 25 years, with emphasis on real property matters. Naturally land lasts longer than people, so estates, trusts and succession issues are relevant.
Local KP is the heart of southern Puget Sound, 75 miles of spectacular residential waterfront. We have the best land, waterfront, beaches and views in Puget Sound, however of course Seattle and the San Juan Islands could not be disregarded. It's that we have the most privacy, the best old growth Doug Firs, wildlife and low population density.
Puget Sound conditions are very specific for residential development.
One must consider:
Topography, hydro-geology, geomorphology, hill slope stability, soils must support septic systems, individual wells, prescriptive, express and implied easement issues, boundary lines don't always line up with surveys or expectations, or historic use, thus adverse possession abounds environmentally protected shorelines and wetlands, all challenges, but ohh.., the views and unique, world class waterfront.
Everyone who lives on Puget Sound is convinced they live in the most beautiful and spectacular place in the world, and we're all correct.

Target Market(s)

Members of the Halvern-Ostrow County Bar Association, and more distant counsel seeking consultation re: local conditions.
Also, I decided it was time to have a website, so a reference place to direct clients.
I like the professional sound of .lawyer vs. commercial sound of .com.

Industry/Entity Type

Law Firm

Coding

Coded - Design and coding required

Number of Pages Required

5+ page

Font styles to use
Other font styles liked:
• That newly created "web" font everyone seems to be usIng

Colors
32b8a4
3377b5

Requirements
Must have
• A strong first page with my photo and Puget Sound chart professionally created.
• A page I have ready with local links.
• A "How to find me page", which should have a map, and photo of my office, which I can make with the preloaded templates the host provides.
• A "This is what I do page", with some testimonials, which I can do via said templates or preferably by professionals.
Nice to have
• Clean look.
• Consistent looks to pages.
• First comment I got back talked about just designing one page, and if requires $340.00, so be it.
• Typical local sites have 4/5 pages, so perhaps a "fill-able" generic pages, I can build myself.
• Ideally, I would step into a working site I can edit myself.
• Not looking for e-commerce site, but the remainder of language the "Smart" professional used is unknown to me.
• Bit out of my element here, hoping for guidance.
Should not have
• Clutter

```html
<!DOCTYPE html>
<html lang="en">
<head>
<meta charset="utf-8">
<title>CedarBight.Lawyer</title>
<link href="https://fonts.googleapis.com/css2?family=Fjalla+One&family=Montserrat:wght@400;700&family=Open+Sans:ital,wght@0,300;0,400;0,600;0,700;1,400&display=swap" rel="stylesheet">
<style>
:root{
  --teal:#32b8a4;
  --teal-soft:#86d5c6;
  --blue:#3377b5;
  --navy:#1f4d82;
  --gold:#f0b323;
  --gold-deep:#e8a317;
  --ink:#222;
  --body:#444;
  --muted:#777;
  --white:#fff;
  --night:#1c1c1c;
}
*{margin:0;padding:0;box-sizing:border-box}
html,body{width:1200px;height:2456px;overflow:hidden}
body{position:relative;background:var(--white);font-family:"Open Sans",sans-serif;color:var(--body)}
.abs{position:absolute}
.heading{font-family:"Fjalla One",sans-serif;font-weight:400}
.btn{position:absolute;display:flex;align-items:center;justify-content:center;font-family:"Montserrat",sans-serif;font-weight:700;font-size:10px;letter-spacing:.5px;text-transform:uppercase;color:var(--ink)}
.btn-gold{background:var(--gold)}
.btn-white{background:var(--white)}

/* header */
.site-header{top:0;left:0;width:1200px;height:54px;background:var(--white);border-top:2px solid var(--gold)}
.brand{position:absolute;left:262px;top:8px;display:flex;align-items:center;gap:8px}
.brand-dot{width:38px;height:38px;border-radius:50%;background:var(--navy)}
.brand-name{font-family:"Fjalla One",sans-serif;font-size:20px;color:var(--navy);line-height:1}
.request-tab{position:absolute;left:784px;top:0;width:159px;height:18px;background:var(--gold);font-family:"Montserrat",sans-serif;font-size:8.5px;font-weight:700;display:flex;align-items:center;justify-content:center;gap:5px;color:var(--ink)}
.main-nav{position:absolute;right:257px;top:29px;display:flex;font-family:"Montserrat",sans-serif;font-size:9px;font-weight:700;color:var(--ink)}
.main-nav span{padding:0 9px;border-left:1px solid #ccc;line-height:11px}
.main-nav span:first-child{border-left:0;color:var(--blue)}
.main-nav span:last-child{padding-right:0}

/* hero */
.hero{top:54px;left:0;width:1200px;height:426px;background:linear-gradient(180deg,#2f3a22 0%,#4a4a2a 30%,#27301e 60%,#121712 100%)}
.hero-arrow{position:absolute;top:196px}
.hero-tag{left:257px;top:188px;height:23px;padding:0 14px 0 8px;background:var(--teal);color:#11302a;font-family:"Fjalla One",sans-serif;font-size:15px;line-height:23px}
.hero-title{left:257px;top:213px;height:50px;padding:0 12px;background:var(--blue);color:var(--white);font-family:"Fjalla One",sans-serif;font-size:38px;line-height:50px;letter-spacing:1px}
.hero-sub{left:267px;top:264px;color:var(--white);font-family:"Montserrat",sans-serif;font-size:18px}
.hero-or{left:432px;top:308px;width:24px;height:24px;border-radius:50%;background:#777;color:#ddd;font-family:"Montserrat",sans-serif;font-size:8px;font-weight:700;display:flex;align-items:center;justify-content:center}
.hero-phone{left:475px;top:303px;display:flex;align-items:center;gap:6px;color:var(--gold);font-family:"Montserrat",sans-serif;font-size:19px;font-weight:700}

/* law office */
.law-office{top:480px;left:0;width:1200px;height:427px;background:linear-gradient(90deg,#f2f2f2 0%,#f6f6f4 45%,#e6e4df 75%,#d2cfc8 100%)}
.law-office-photo{position:absolute;left:0;top:0;width:475px;height:427px;background:linear-gradient(160deg,#e6e6e6 0%,#cfd2d6 45%,#6d6f73 75%,#3e4046 100%)}
.seal{left:552px;top:432px;width:96px;height:96px;border-radius:50%;background:rgba(255,255,255,.55);display:flex;align-items:center;justify-content:center}
.seal span{width:58px;height:58px;border-radius:50%;background:var(--navy);display:block}
.section-title{width:1200px;text-align:center;color:var(--ink);font-size:32px}
.section-sub{width:1200px;text-align:center;font-family:"Fjalla One",sans-serif;font-size:11px;color:var(--blue)}
.office-title{left:0;top:535px}
.office-sub{left:0;top:579px}
.office-head{left:491px;top:622px;font-size:27px;font-weight:300;color:var(--ink);letter-spacing:.3px}
.office-kicker{left:492px;top:655px;font-size:10.5px;font-weight:700;color:var(--ink)}
.office-text{left:492px;width:448px;font-size:10.5px;line-height:14.5px;color:#555}

/* practice areas */
.practice-band{top:907px;left:0;width:1200px;height:141px;background:linear-gradient(180deg,#4677a8 0%,#6d93b8 35%,#9bb3c8 50%,#4c7bab 62%,#2f6097 100%)}
.practice-title{left:0;top:962px;color:var(--white)}
.practice-sub{left:0;top:1005px;color:var(--white)}
.practice-grid{top:1048px;left:0;width:1200px;height:285px}
.tile{position:absolute;width:300px;overflow:hidden}
.tile-photo{position:absolute}
.card{position:absolute;background:var(--white);padding:14px 12px 0 12px}
.card h3{font-family:"Fjalla One",sans-serif;font-weight:400;font-size:16px;color:var(--ink);margin-bottom:6px}
.card p{font-size:9.4px;line-height:14px;color:#444}
.card p em{font-style:normal;color:var(--blue)}
.card .btn{position:static;width:88px;height:22px;margin-top:8px}
.card-teal{background:var(--teal-soft)}
.card-teal h3{color:#fff}
.card-teal p{color:#e8f7f3}
.card-teal .btn{background:#8bb88a;color:#d6ead6}
.notch{position:absolute;width:0;height:0;border-left:9px solid transparent;border-right:9px solid transparent}
.zoom{left:701px;top:1166px;width:58px;height:58px;border-radius:50%;background:rgba(120,210,190,.75);display:flex;align-items:center;justify-content:center}
.slider-band{top:1333px;left:0;width:1200px;height:78px;background:var(--navy)}
.slider-dots{left:558px;top:1349px;display:flex;gap:6px}
.slider-dots span{width:24px;height:3px;background:var(--white)}
.slider-dots span:first-child{background:var(--teal)}

/* results */
.results{top:1411px;left:0;width:1200px;height:133px;background:linear-gradient(180deg,var(--gold) 0%,#f2bb35 60%,var(--gold-deep) 100%)}
.results-title{left:301px;top:1446px;font-size:34px;color:var(--ink)}
.results-sub{left:430px;top:1484px;width:218px;text-align:right;font-size:12px;color:var(--ink)}
.results-btn{left:697px;top:1442px;width:148px;height:28px}
.results-phone{left:700px;top:1486px;display:flex;align-items:center;gap:8px;color:var(--ink);font-family:"Montserrat",sans-serif;font-size:18px;font-weight:700}

/* testimonials */
.testimonials{top:1544px;left:0;width:1200px;height:465px;background:linear-gradient(180deg,#3a2a2a 0%,#6c3a2a 30%,#b7532d 55%,#6a2f22 78%,#1f1615 100%)}
.testi-title{left:0;top:1598px;color:var(--white)}
.testi-sub{left:0;top:1642px;color:var(--white)}
.quote{position:absolute;left:408px;width:384px;height:105px;background:#f4f4f4;box-shadow:0 2px 6px rgba(0,0,0,.35);padding:14px 30px 0;text-align:center}
.quote p{font-style:italic;font-size:13px;line-height:18px;color:#777}
.quote cite{display:block;margin-top:10px;font-family:"Fjalla One",sans-serif;font-style:normal;font-size:10.5px;color:var(--blue)}
.quote-tail{position:absolute;top:44px;width:0;height:0;border-top:9px solid transparent;border-bottom:9px solid transparent}
.avatar{position:absolute;width:130px;height:130px;border-radius:50%;border:7px solid #2e5e8e}

/* contact strip */
.contact-strip{top:2009px;left:0;width:1200px;height:116px;background:var(--white)}
.office-address{left:258px;top:2034px;width:220px;text-align:center;font-size:8.6px;line-height:12px;color:#444}
.office-address strong,.need-help strong{display:block;font-size:10.5px;margin-bottom:4px;color:var(--ink)}
.footer-brand{left:536px;top:2046px;display:flex;align-items:center;gap:8px}
.footer-brand .brand-dot{width:40px;height:40px}
.footer-brand .brand-name{font-size:20px}
.need-help{left:733px;top:2034px;width:200px;text-align:center;font-size:10.5px;line-height:17px;color:#444}

.map{top:2125px;left:0;width:1200px;height:241px;background:linear-gradient(90deg,#a9d3f0 0%,#b8dcf2 28%,#dfe8c8 45%,#cfe0b3 60%,#d8e4bd 80%,#c8dcaa 100%)}

/* bottom bar */
.bottom-bar{top:2366px;left:0;width:1200px;height:90px;background:var(--night)}
.bottom-links{left:257px;top:2380px;font-size:9px;font-weight:600;color:#ddd}
.copyright{left:257px;top:2408px;font-size:9px;color:#999}
.social{left:806px;top:2399px;display:flex;gap:6px}
.social span{width:22px;height:22px;border-radius:50%;background:#4a6a8c;display:block}
</style>
</head>
<body>

<header class="abs site-header">
  <div class="brand"><span class="brand-dot"></span><span class="brand-name">CEDARBIGHT LAWYER</span></div>
  <div class="request-tab">
    <svg width="9" height="7" viewBox="0 0 9 7"><rect x=".5" y=".5" width="8" height="6" fill="none" stroke="#222"/><path d="M.5.5 4.5 4 8.5.5" fill="none" stroke="#222"/></svg>
    REQUEST FREE CONSULTATION
  </div>
  <nav class="main-nav"><span>HOME</span><span>MY LAW OFFICE</span><span>PRACTICE AREAS</span><span>TESTIMONIALS</span><span>CONTACT US</span></nav>
</header>

<section class="abs hero" role="img" aria-label="Evening photo of a quiet forest lake framed by fir trees">
  <svg class="hero-arrow" style="left:30px" width="20" height="38" viewBox="0 0 20 38"><path d="M18 1 2 19l16 18" fill="none" stroke="#ccc" stroke-width="1.5"/></svg>
  <svg class="hero-arrow" style="left:1150px" width="20" height="38" viewBox="0 0 20 38"><path d="M2 1l16 18L2 37" fill="none" stroke="#ccc" stroke-width="1.5"/></svg>
</section>
<div class="abs hero-tag">Housands of Cases Successfully Handled</div>
<div class="abs hero-title">CEDARBIGHT LAWYER</div>
<div class="abs hero-sub">Estates, Trusts &amp; Succession Issues Are Relevant</div>
<div class="btn btn-gold" style="left:268px;top:357px;width:146px;height:31px">Free Consultation</div>
<div class="abs hero-or">OR</div>
<div class="abs hero-phone">
  <svg width="26" height="26" viewBox="0 0 24 24"><path d="M6.6 10.8a15 15 0 0 0 6.6 6.6l2.2-2.2c.3-.3.7-.4 1-.2 1.1.4 2.3.6 3.6.6.6 0 1 .4 1 1V20c0 .6-.4 1-1 1A17 17 0 0 1 3 4c0-.6.4-1 1-1h3.5c.6 0 1 .4 1 1 0 1.3.2 2.5.6 3.6.1.3 0 .7-.2 1z" fill="#f0b323"/><path d="M14 3a7 7 0 0 1 7 7M14 6.5A3.5 3.5 0 0 1 17.5 10" stroke="#f0b323" stroke-width="1.6" fill="none"/></svg>
  +1.555.014.2290
</div>

<section class="abs law-office">
  <div class="law-office-photo" role="img" aria-label="Portrait of the attorney seated at his office desk"></div>
</section>
<div class="abs seal"><span></span></div>
<h2 class="abs heading section-title office-title">My Law Office</h2>
<div class="abs section-sub office-sub">A GOOD FIT FOR YOU?</div>
<h3 class="abs office-head">WHO WE WON'T REPRESENT</h3>
<div class="abs office-kicker">A CLEAR UNDERSTANDING OF A LAW FIRM'S PRACTICE LIMITS</div>
<p class="abs office-text" style="top:681px">Lorem ipsum dolor sit amet, consectetur adipisicing elit, sed do eiusmod tempor incididunt ut labore et dolore magna aliqua. Ut enim ad minim veniam, quis nostrud exercitation ullamco laboris nisi ut aliquip ex ea commodo consequat. Duis aute irure dolor in reprehenderit in voluptate velit esse cillum dolore.</p>
<p class="abs office-text" style="top:753px">Lorem ipsum dolor sit amet, consectetur adipisicing elit, sed do eiusmod tempor incididunt ut labore et dolore magna aliqua. Ut enim ad minim veniam, quis nostrud exercitation ullamco laboris nisi ut aliquip</p>
<div class="btn btn-gold" style="left:493px;top:817px;width:97px;height:27px">Learn More</div>

<section class="abs practice-band" role="img" aria-label="Photo of the sound with snowy mountains across the water"></section>
<h2 class="abs heading section-title practice-title">Practice Areas</h2>
<div class="abs section-sub practice-sub">WHAT CAN WE HELP YOU WITH?</div>

<section class="abs practice-grid">
  <div class="tile" style="left:0;top:0;height:285px">
    <div class="tile-photo" role="img" aria-label="Photo of a rural office building among shrubs" style="left:0;top:0;width:300px;height:134px;background:linear-gradient(180deg,#c9ccc6 0%,#6f5a44 45%,#3f3a2c 100%)"></div>
    <div class="card" style="left:0;top:134px;width:300px;height:151px">
      <h3>Emphasis on real property matters</h3>
      <p>Lorem ipsum dolor sit amet, consectetur adipisicing elit, sed do eiusmod tempor <em>incididunt ut labore et dolore magna aliqua.</em> Ut enim ad minim veniam, quis nostrud exercitation ullamco laboris nisi ut aliquip ex ea commodo consequat. Duis aute irure dolor in reprehenderit in</p>
      <div class="btn btn-gold">Read More</div>
    </div>
    <div class="notch" style="left:150px;top:125px;border-bottom:9px solid #fff"></div>
  </div>

  <div class="tile" style="left:300px;top:0;height:285px">
    <div class="card" style="left:0;top:0;width:300px;height:134px">
      <h3>Naturally land lasts longer than people</h3>
      <p>Lorem ipsum dolor sit amet, consectetur adipisicing elit, sed do eiusmod tempor <em>incididunt ut labore et dolore magna aliqua.</em> Ut enim ad minim veniam, quis nostrud exercitation ullamco laboris nisi ut aliquip ex ea commodo consequat. Duis aute irure dolor in reprehenderit in</p>
      <div class="btn btn-gold">Read More</div>
    </div>
    <div class="tile-photo" role="img" aria-label="Photo of a calm lake reflecting a wooded shore" style="left:0;top:134px;width:300px;height:151px;background:linear-gradient(180deg,#b7c9dc 0%,#6f8fb0 45%,#2f4a66 75%,#4a4a3c 100%)"></div>
    <div class="notch" style="left:141px;top:134px;border-top:9px solid #fff;border-bottom:0"></div>
  </div>

  <div class="tile" style="left:600px;top:0;height:285px">
    <div class="tile-photo" role="img" aria-label="Photo of a teal evening sky over shoreline trees" style="left:0;top:0;width:300px;height:134px;background:linear-gradient(180deg,#5fb7b0 0%,#8fd0c2 55%,#3a6a60 100%)"></div>
    <div class="card card-teal" style="left:0;top:134px;width:300px;height:151px">
      <h3>Estates, trusts and succession issues</h3>
      <p>Lorem ipsum dolor sit amet, consectetur adipisicing elit, sed do eiusmod tempor incididunt ut labore et dolore magna aliqua. Ut enim ad minim veniam, quis nostrud exercitation ullamco laboris nisi ut aliquip ex ea commodo consequat. Duis aute irure dolor in reprehenderit in</p>
      <div class="btn">Read More</div>
    </div>
  </div>

  <div class="tile" style="left:900px;top:0;height:285px">
    <div class="card" style="left:0;top:0;width:300px;height:134px">
      <h3>Real property matters</h3>
      <p>Lorem ipsum dolor sit amet, consectetur adipisicing elit, sed do eiusmod tempor <em>incididunt ut labore et dolore magna aliqua.</em> Ut enim ad minim veniam, quis nostrud exercitation ullamco laboris nisi ut aliquip ex ea commodo consequat. Duis aute irure dolor in reprehenderit in</p>
      <div class="btn btn-gold">Read More</div>
    </div>
    <div class="tile-photo" role="img" aria-label="Photo of a stone wall beside dry brush" style="left:0;top:134px;width:300px;height:151px;background:linear-gradient(180deg,#7a7560 0%,#9a8c6e 45%,#c9c6bd 70%,#a9a59a 100%)"></div>
    <div class="notch" style="left:141px;top:134px;border-top:9px solid #fff;border-bottom:0"></div>
  </div>
</section>
<div class="abs zoom">
  <svg width="24" height="24" viewBox="0 0 24 24"><circle cx="11" cy="11" r="8" fill="none" stroke="#fff" stroke-width="2"/><path d="M11 7v8M7 11h8M17 17l5 5" stroke="#fff" stroke-width="2"/></svg>
</div>

<section class="abs slider-band"></section>
<div class="abs slider-dots"><span></span><span></span><span></span></div>

<section class="abs results"></section>
<h2 class="abs heading results-title">REAL RESULTS. OUR VICTORIES.</h2>
<div class="abs results-sub">When you work with us, <strong>we promise.</strong></div>
<div class="btn btn-white results-btn">Free Consultation</div>
<div class="abs results-phone">
  <svg width="24" height="24" viewBox="0 0 24 24"><path d="M6.6 10.8a15 15 0 0 0 6.6 6.6l2.2-2.2c.3-.3.7-.4 1-.2 1.1.4 2.3.6 3.6.6.6 0 1 .4 1 1V20c0 .6-.4 1-1 1A17 17 0 0 1 3 4c0-.6.4-1 1-1h3.5c.6 0 1 .4 1 1 0 1.3.2 2.5.6 3.6.1.3 0 .7-.2 1z" fill="#fff"/><path d="M14 3a7 7 0 0 1 7 7M14 6.5A3.5 3.5 0 0 1 17.5 10" stroke="#fff" stroke-width="1.6" fill="none"/></svg>
  +1.555.014.2290
</div>

<section class="abs testimonials" role="img" aria-label="Photo of a red sunset over the water with silhouetted fir trees"></section>
<h2 class="abs heading section-title testi-title">Testimonials</h2>
<div class="abs section-sub testi-sub">Our Awesome Success Stories</div>

<div class="avatar" style="left:249px;top:1665px;background:linear-gradient(180deg,#5f8fb7 0%,#c7764a 100%)" role="img" aria-label="Portrait photo of a client"></div>
<blockquote class="quote" style="top:1681px">
  <span class="quote-tail" style="left:-9px;border-right:9px solid #f4f4f4"></span>
  <p>Lorem ipsum dolor sit amet, consectetur adipisicing elit, sed do eiusmod tempor incididunt ut labore et dolore magna aliqua.</p>
  <cite>– Dana Whitcombe, Founder of Larkfield Media</cite>
</blockquote>

<blockquote class="quote" style="top:1832px">
  <span class="quote-tail" style="right:-9px;border-left:9px solid #f4f4f4"></span>
  <p>Lorem ipsum dolor sit amet, consectetur adipisicing elit, sed do eiusmod tempor incididunt ut labore et dolore magna aliqua.</p>
  <cite>– Lee Harrowgate, Founder of Ostrel Co</cite>
</blockquote>
<div class="avatar" style="left:819px;top:1821px;background:linear-gradient(180deg,#e9edf1 0%,#8fb3d6 100%)" role="img" aria-label="Portrait photo of a client"></div>

<section class="abs contact-strip"></section>
<div class="abs office-address">
  <strong>LAW OFFICE</strong>
  4127 Harrow Point Rd N.,<br>(next to the Fire Station in the Library/Professional<br>Services Building, physically the town of Alder Crossing),<br>Fenwick Bay, WA 98000.
</div>
<div class="abs footer-brand"><span class="brand-dot"></span><span class="brand-name">CEDARBIGHT LAWYER</span></div>
<div class="abs need-help">
  <strong>NEED HELP!</strong>
  Email Us: morris@cedarbight.lawyer<br>Call Us: +1.555.014.2290
</div>

<section class="abs map" role="img" aria-label="Road map of the southern sound region showing the office location"></section>

<footer class="abs bottom-bar"></footer>
<div class="abs bottom-links">Home / My Law Office / Practice Areas / Testimonials / Contact Us</div>
<div class="abs copyright">© 2015-16. Morris P. Halden, Attorney at Law. All Rights Reserved.</div>
<div class="abs social"><span></span><span></span><span></span><span></span><span></span></div>

</body>
</html>
```